Welding Fabrication and Inspection Business Card Design

Welding Fabrication and Inspection Services,

Business

Industrial Machinery ServicesMohammed Rahim30 Ballarat Street, Mount Gravatt East.4122.QLD

```html
<!DOCTYPE html>
<html lang="en">
<head>
<meta charset="utf-8">
<title>Tarnwell Forge Services – Business Card</title>
<link href="https://fonts.googleapis.com/css2?family=Open+Sans:wght@400;600;700;800&display=swap" rel="stylesheet">
<style>
  :root {
    --brand-red: #d40f1a;
    --brand-red-dark: #c4000d;
    --card-white: #ffffff;
    --ink: #161616;
    --muted: #9a9a9a;
    --spark: #ffe11a;
    --bg-light: #d6d6d6;
    --bg-dark: #6e6e6e;
  }
  * { box-sizing: border-box; margin: 0; padding: 0; }
  html, body { width: 1200px; height: 960px; overflow: hidden; }
  body {
    background: radial-gradient(ellipse at 40% 35%, var(--bg-light) 0%, #a9a9a9 55%, var(--bg-dark) 100%);
    font-family: "Open Sans", Arial, sans-serif;
    position: relative;
  }
  .card {
    position: absolute;
    top: 330px;
    width: 520px;
    height: 298px;
    overflow: hidden;
    box-shadow: 0 14px 30px rgba(0,0,0,0.28);
  }
  /* Front */
  .card-front {
    left: 50px;
    background: linear-gradient(135deg, var(--brand-red) 0%, var(--brand-red-dark) 100%);
    display: flex;
    align-items: center;
    justify-content: center;
  }
  .wordmark {
    display: flex;
    align-items: center;
    gap: 14px;
    color: var(--card-white);
    font-weight: 800;
    font-size: 30px;
    letter-spacing: 0.5px;
  }
  .wordmark-dot {
    width: 26px; height: 26px;
    border-radius: 50%;
    background: var(--spark);
    flex: none;
  }
  /* Back */
  .card-back { left: 630px; background: var(--card-white); }
  .back-logo {
    position: absolute;
    top: 48px; left: 86px;
    display: flex; align-items: center; gap: 10px;
    color: var(--brand-red);
    font-weight: 800;
    font-size: 20px;
  }
  .back-logo .wordmark-dot { width: 16px; height: 16px; }
  .holder {
    position: absolute;
    top: 112px; right: 34px;
    text-align: right;
  }
  .holder-name { font-weight: 700; font-size: 21px; color: var(--ink); letter-spacing: 0.5px; }
  .holder-title { font-size: 13px; color: var(--muted); margin-top: 2px; }
  .band {
    position: absolute;
    left: 0; bottom: 0;
    width: 100%; height: 130px;
  }
  .contacts {
    position: absolute;
    left: 26px; bottom: 22px;
    color: var(--card-white);
    font-size: 12.5px;
    line-height: 1.75;
  }
  .contact-row { display: flex; align-items: center; gap: 22px; }
  .contact-item { display: flex; align-items: center; gap: 7px; }
  .contact-item svg { width: 11px; height: 11px; fill: var(--card-white); flex: none; }
</style>
</head>
<body>

  <section class="card card-front" aria-label="Card front">
    <div class="wordmark"><span class="wordmark-dot"></span>Tarnwell Forge Services</div>
  </section>

  <section class="card card-back" aria-label="Card back">
    <div class="back-logo"><span class="wordmark-dot"></span>Tarnwell Forge Services</div>

    <div class="holder">
      <div class="holder-name">Khalid Nasser</div>
      <div class="holder-title">Title</div>
    </div>

    <svg class="band" viewBox="0 0 520 130" preserveAspectRatio="none" aria-hidden="true">
      <polygon points="0,0 70,0 80,12 90,0 520,0 520,130 0,130" fill="var(--brand-red-dark)"/>
    </svg>

    <div class="contacts">
      <div class="contact-item">
        <svg viewBox="0 0 10 10"><path d="M5 0a3.5 3.5 0 0 0-3.5 3.5C1.5 6 5 10 5 10s3.5-4 3.5-6.5A3.5 3.5 0 0 0 5 0zm0 5a1.5 1.5 0 1 1 0-3 1.5 1.5 0 0 1 0 3z"/></svg>
        17 Corrowen Street, Pellham Rise, 4190, QLD
      </div>
      <div class="contact-row">
        <div class="contact-item">
          <svg viewBox="0 0 10 10"><path d="M2 0l2 2.5-1 1.2c.6 1.3 1.5 2.2 2.8 2.8L7 5.5 9.5 7.5 8.3 9.6C4 9.6.4 6 .4 1.7z"/></svg>
          303-555-0148
        </div>
        <div class="contact-item">
          <svg viewBox="0 0 10 10"><rect x="2.5" y="0" width="5" height="10" rx="1"/></svg>
          303-555-0172
        </div>
      </div>
      <div class="contact-row">
        <div class="contact-item">
          <svg viewBox="0 0 10 10"><path d="M0 2h10v6H0zM0 2l5 3.5L10 2" stroke="#c4000d" stroke-width="0.8"/></svg>
          khalid@tarnwellforge.example
        </div>
        <div class="contact-item">
          <svg viewBox="0 0 10 10"><circle cx="5" cy="5" r="5"/></svg>
          @tarnwellforge
        </div>
      </div>
    </div>
  </section>

</body>
</html>
```